CalmPath Nurses' Manifesto

Design a manifesto to inspire and motivate nurses to work at minimum standards of excellence in their nursing practice.

The manifesto will become a feature of our website, at conferences, workshops and retreats. It will also be featured on other marketing tools.

Primary Market:
Nurses and/or other healthcare professionals (specifically Doctors, Occupational Therapists, Psychologists and Social Workers).

However the manifesto is equally applicable to all nurses and healthcare professionals from new graduates to very experienced senior clinicians, administration officers,managers and healthcare executive personnel.

Mainly females and primarily 35 to 65 years old, which suggests people in this target age group have extensive experience, but have become jaded'.

The purpose of our business is to assist healthcare professionals, primarily nurses, to maintain their enthusiasm and excellence in service provision, for their benefit as well as the benefit of the clients.

I have attached:
File 1: Copy Samples and examples: which has the copy for the manifesto, examples that appeal to us and our 3 attempts.
File 2: Our colour Spec Sheet, HOWEVER the colours are not necessary limited to these colours. These colours are not in the logo that will be on the manifesto. The colours on the logo attached can/or also be used.
File 3: Prototype logo. The final logo will be available within 3 to 4 days.

Requirements
Must have
• Must use the copy as per the attached file.

It should be contemporary, eye catching and motivational.

Sample 1 on the attached file (File 3: copy, samples and examples_554207 saturday, 29 june 2013 06:24:3030) Is close to what we are looking for.
Should not have
• MUST BE EASY TO READ. Each line MUST be clearly defined from each other.

```html
<!DOCTYPE html>
<html lang="en">
<head>
<meta charset="utf-8">
<title>CalmPath Nurses' Manifesto</title>
<link rel="stylesheet" href="https://fonts.googleapis.com/css2?family=Open+Sans:wght@400;600;700&display=swap">
<style>
:root{
  --blue:#4fa0e2;
  --blue-deep:#3b6fd6;
  --sky:#47aee8;
  --green:#8cc63f;
  --lime:#9ccd2e;
  --purple:#9b3fc7;
  --violet:#7a3fd1;
  --magenta:#e0218a;
  --orchid:#c83ac9;
  --red:#e8262c;
  --orange:#f39019;
  --brown:#7a4516;
  --teal:#52c7b8;
  --ink:#1e1e1e;
  --grey:#666a6d;
  --grey-soft:#9ca0a3;
  --grey-pale:#b9bcbe;
  --white:#ffffff;
}
*{margin:0;padding:0;box-sizing:border-box}
html,body{width:900px;height:1200px;overflow:hidden;background:var(--white)}
.manifesto{position:relative;width:900px;height:1200px;font-family:"Open Sans",Arial,sans-serif;color:var(--grey);overflow:hidden}
.line{position:absolute;white-space:nowrap;line-height:1}
.spread{display:flex;justify-content:space-between;align-items:baseline}
.up{transform:rotate(-90deg);transform-origin:0 0}
.down{transform:rotate(90deg);transform-origin:0 0}
.top-band{position:absolute;left:38px;top:0;width:840px;height:12px;background:var(--blue)}
.photo-nurse{position:absolute;left:632px;top:810px;width:258px;height:390px;background:linear-gradient(180deg,#f4efe9 0%,#cfe9ea 45%,#8fd0d2 100%);border-radius:110px 110px 0 0}
.foot-left{position:absolute;left:38px;top:1138px;width:10px;height:62px;background:var(--blue)}
.foot-band{position:absolute;left:515px;top:1138px;width:363px;height:62px;background:var(--blue)}
.foot-band .slogan{position:absolute;left:10px;top:12px;color:var(--white);font-size:30px;line-height:1;white-space:nowrap}
.foot-band .slogan b{font-size:38px;font-weight:400}
.brand{position:absolute;left:62px;top:1146px;display:flex;align-items:center;gap:10px}
.brand .mark{width:38px;height:38px;background:var(--green)}
.brand .name{font-size:22px;color:var(--ink)}
.c-blue{color:var(--blue)} .c-deep{color:var(--blue-deep)} .c-sky{color:var(--sky)}
.c-green{color:var(--green)} .c-lime{color:var(--lime)} .c-purple{color:var(--purple)}
.c-violet{color:var(--violet)} .c-mag{color:var(--magenta)} .c-orchid{color:var(--orchid)} .c-red{color:var(--red)}
.c-orange{color:var(--orange)} .c-brown{color:var(--brown)} .c-teal{color:var(--teal)}
.c-ink{color:var(--ink)} .c-grey{color:var(--grey)} .c-soft{color:var(--grey-soft)} .c-pale{color:var(--grey-pale)}
.bold{font-weight:700}
.lifelong .tail{vertical-align:top;font-size:33px}
</style>
</head>
<body>
<main class="manifesto">
  <div class="top-band"></div>
  <div class="photo-nurse" role="img" aria-label="Photograph of a smiling nurse in light blue scrubs holding a clipboard"></div>
  <div class="foot-left"></div>
  <div class="foot-band"><p class="slogan">Live your <b>dream.</b></p></div>
  <div class="brand"><span class="mark"></span><span class="name">CalmPath</span></div>

  <!-- Header -->
  <p class="line c-blue" style="left:38px;top:20px;font-size:70px">Nurse</p>
  <p class="line" style="left:248px;top:16px;font-size:52px"><span class="c-green" style="font-size:28px">Deliver</span> <span class="c-blue">care</span> <span class="c-green" style="font-size:28px">skillfully.</span></p>
  <p class="line c-blue" style="left:630px;top:12px;font-size:100px">Trust</p>
  <p class="line" style="left:246px;top:66px;font-size:46px"><span class="c-green">Learn</span> <span class="c-ink" style="font-size:28px">something</span></p>
  <p class="line c-purple" style="left:38px;top:97px;font-size:40px">with open</p>
  <p class="line spread c-ink" style="left:248px;top:116px;width:310px;font-size:28px"><span>new</span><span>each</span><span>day.</span></p>
  <p class="line c-grey" style="left:36px;top:140px;font-size:48px">hands, hearts and minds.</p>

  <!-- Be a lifelong learner -->
  <p class="line down lifelong c-deep" style="left:642px;top:76px;font-size:48px">Be <span class="tail">a lifelong learner.</span></p>

  <!-- Right top column -->
  <p class="line c-mag" style="left:656px;top:116px;font-size:29px">Celebrate,</p>
  <p class="line c-deep" style="left:656px;top:152px;font-size:27px">respect <span style="font-size:21px">and</span></p>
  <p class="line c-orange" style="left:656px;top:186px;font-size:27px;letter-spacing:12px">value</p>
  <p class="line spread c-deep" style="left:656px;top:225px;width:152px;font-size:22px"><span>the</span><span>diversity</span></p>
  <p class="line spread c-deep" style="left:656px;top:259px;width:152px;font-size:22px"><span>of</span><span>Australian</span></p>
  <p class="line c-deep" style="left:656px;top:293px;font-size:22px;letter-spacing:7px">culture.</p>
  <p class="line c-mag" style="left:656px;top:326px;font-size:42px">Choose</p>
  <p class="line c-pale" style="left:656px;top:368px;font-size:20px;letter-spacing:5px">thoughts</p>
  <p class="line spread c-pale" style="left:656px;top:390px;width:152px;font-size:20px"><span>wisely,</span><span>they</span></p>
  <p class="line spread c-pale" style="left:656px;top:412px;width:152px;font-size:20px"><span>create</span><span>your</span></p>
  <p class="line c-mag" style="left:656px;top:432px;font-size:42px;letter-spacing:3px">reality<span class="c-ink">.</span></p>
  <p class="line up c-ink spread" style="left:818px;top:494px;width:405px;font-size:22px"><span>your</span><span>knowledge</span><span>and</span><span>seek</span><span>advice</span></p>
  <p class="line up c-ink spread" style="left:843px;top:494px;width:405px;font-size:22px"><span>only</span><span>from</span><span>respected</span><span>sources.</span></p>

  <!-- Left body -->
  <p class="line" style="left:40px;top:198px;font-size:38px"><span class="c-grey" style="font-size:28px;letter-spacing:1px">Look&nbsp;&nbsp;&nbsp;&nbsp;after</span> <span class="c-mag">yourself</span></p>
  <p class="line" style="left:40px;top:242px;font-size:38px"><span class="c-grey" style="font-size:28px">and value your</span> <span class="c-sky">health</span></p>
  <p class="line spread c-grey" style="left:40px;top:292px;width:346px;font-size:28px"><span>as</span><span>much</span><span>as</span><span>you</span><span>value</span></p>
  <p class="line spread c-grey" style="left:40px;top:338px;width:346px;font-size:28px"><span>the</span><span>health</span><span>of</span><span>others.</span></p>
  <p class="line" style="left:38px;top:372px;font-size:48px"><span class="c-red">Respect</span>&nbsp; <span class="c-grey" style="font-size:21px">the <span class="c-green">limits</span> of</span></p>
  <p class="line c-grey" style="left:40px;top:438px;font-size:21px"><span class="c-deep">people</span>’s knowledge and share</p>
  <p class="line spread c-ink" style="left:40px;top:484px;width:346px;font-size:21px"><span>your</span><span>knowledge</span><span>generously.</span></p>

  <!-- Vertical support block -->
  <p class="line up c-purple" style="left:396px;top:862px;font-size:42px">Delight <span style="font-size:36px">your clients and</span> <span class="c-teal">colleagues</span></p>
  <p class="line up c-grey" style="left:444px;top:862px;font-size:28px">by exceeding their expectations. <span class="c-brown" style="font-size:52px">Support</span></p>
  <p class="line up c-soft" style="left:499px;top:862px;font-size:29px;letter-spacing:0.6px">your colleagues and champion their purpose.</p>
  <p class="line up c-mag" style="left:546px;top:472px;font-size:24px">be solution focused.</p>

  <!-- Smile block -->
  <p class="line up c-blue" style="left:38px;top:836px;font-size:46px">Smile <span class="c-soft" style="font-size:22px">and</span> <span class="c-mag">infect</span></p>
  <p class="line up c-ink" style="left:90px;top:700px;font-size:20px">others with your</p>
  <p class="line up c-blue" style="left:108px;top:700px;font-size:42px">happiness</p>
  <p class="line up c-ink" style="left:160px;top:700px;font-size:20px">and have <span class="c-orange" style="font-size:28px">fun</span>!</p>

  <!-- You are unique -->
  <p class="line" style="left:220px;top:524px;font-size:46px"><span class="c-deep">You</span> <span class="c-pale" style="font-size:26px">are</span></p>
  <p class="line c-purple" style="left:196px;top:574px;font-size:54px">unique<span class="c-orange" style="font-size:30px">,</span></p>
  <p class="line spread c-soft" style="left:196px;top:640px;width:186px;font-size:27px"><span>revel</span><span style="font-size:20px">in</span><span>your</span></p>
  <p class="line c-deep" style="left:196px;top:676px;font-size:28px">individuality.</p>
  <p class="line" style="left:92px;top:712px;font-size:40px"><span class="c-red">Adopt</span> <span class="c-pale" style="font-size:24px">a</span> <span class="c-orange">‘can do’</span></p>
  <p class="line spread c-pale" style="left:146px;top:758px;width:234px;font-size:26px"><span>attitude</span><span>to</span></p>
  <p class="line spread c-pale" style="left:146px;top:787px;width:234px;font-size:26px"><span>everything</span><span>that</span></p>
  <p class="line c-pale" style="left:146px;top:816px;font-size:26px">comes your way.</p>
  <p class="line spread c-ink" style="left:40px;top:846px;width:348px;font-size:28px"><span>firstly</span><span>from</span><span>within.</span></p>
  <p class="line c-lime" style="left:38px;top:872px;font-size:57px"><span class="bold">Seek</span> success</p>
  <p class="line" style="left:38px;top:930px;font-size:50px"><span class="c-soft" style="font-size:28px">Only</span> <span class="c-violet">follow</span> <span class="c-soft" style="font-size:28px">exceptional</span> <span class="c-violet">leaders</span><span class="c-soft">.</span></p>
  <p class="line c-sky" style="left:40px;top:986px;font-size:26px">If there is no one left</p>
  <p class="line" style="left:40px;top:1016px;font-size:48px"><span class="c-sky" style="font-size:26px">to follow, then</span> <span class="c-violet">lead</span><span class="c-sky" style="font-size:26px">!</span></p>
  <p class="line c-orange" style="left:372px;top:994px;font-size:48px">Always</p>
  <p class="line up c-brown" style="left:544px;top:1066px;font-size:36px;height:40px">lead</p>
  <p class="line up c-brown" style="left:586px;top:1066px;font-size:36px;height:40px">with</p>
  <p class="line c-orchid" style="left:38px;top:1064px;font-size:39px">purpose<span class="c-sky">,</span> passion <span style="font-size:24px">and</span> commitment<span class="c-sky">.</span></p>

  <!-- Right middle -->
  <p class="line" style="left:536px;top:492px;font-size:48px"><span class="c-lime">Always</span>&nbsp;&nbsp; <span class="c-purple" style="font-size:24px">do the right</span></p>
  <p class="line spread c-purple" style="left:536px;top:548px;width:330px;font-size:22px"><span>thing</span><span>without</span><span>exception.</span></p>
  <p class="line c-sky" style="left:534px;top:576px;font-size:66px">Respond</p>
  <p class="line c-soft" style="left:836px;top:604px;font-size:26px">to</p>
  <p class="line spread c-pale" style="left:536px;top:644px;width:328px;font-size:26px"><span>complex</span><span>situations</span></p>
  <p class="line up c-ink" style="left:536px;top:872px;font-size:30px">innovatively,</p>
  <p class="line up c-ink" style="left:576px;top:872px;font-size:27px">creatively <span style="font-size:18px">and</span></p>
  <p class="line c-grey" style="left:628px;top:720px;font-size:30px">within the scope</p>
  <p class="line c-grey" style="left:628px;top:762px;font-size:30px">of your practice.</p>
  <p class="line c-ink" style="left:536px;top:884px;font-size:30px">safely</p>
</main>
</body>
</html>
```